Corvale Spine & Joint Business Card

Need a business card using the logo provided. I want brand side of the card to be grey with the logo in the center of the card in white.

On the other side I leave to the designers

Target Market(s)

Personal Injury Attorneys

Industry/Entity Type

Medical

Contact Information for Business Card

Name, CEO. Cell Phone, (Hialeah, Address, Phone) (Homestead, Address, Phone) (Tallahassee, Address, Phone)

Colors

Designer to choose only greyscale colors for use in the design.

Requirements
Must have
• Logo by itself on one side

```html
<!DOCTYPE html>
<html lang="en">
<head>
<meta charset="utf-8">
<title>Corvale Spine &amp; Joint — Business Card</title>
<link rel="stylesheet" href="https://fonts.googleapis.com/css2?family=Montserrat:wght@300;500;600&family=Jost:wght@400&display=swap">
<style>
  :root {
    --backdrop: #3b3b3b;
    --card-white: #ffffff;
    --brand-tint: #9bb8bf;
    --name-grey: #666666;
    --pattern-light: #f1f1f1;
    --on-brand: #ffffff;
  }
  html, body {
    margin: 0;
    width: 1200px;
    height: 900px;
    overflow: hidden;
    background: var(--backdrop);
  }
  .stage {
    position: relative;
    width: 1200px;
    height: 900px;
  }
  .card {
    position: absolute;
    overflow: hidden;
  }
  .card--front {
    left: 271px; top: 45px; width: 672px; height: 383px;
    background: var(--card-white);
  }
  .card--back {
    left: 271px; top: 450px; width: 676px; height: 387px;
    background: var(--brand-tint);
  }
  .card__pattern {
    position: absolute; inset: 0;
    background: linear-gradient(135deg, var(--card-white) 0%, var(--pattern-light) 50%, var(--card-white) 100%);
  }
  .wordmark {
    position: absolute;
    left: 0; right: 0;
    text-align: center;
    font-family: "Montserrat", sans-serif;
    font-weight: 500;
    line-height: 1;
  }
  .wordmark__name { display: block; letter-spacing: 0.06em; }
  .wordmark__tag { display: block; letter-spacing: 0.07em; }
  .card--front .wordmark { top: 48px; color: var(--brand-tint); padding-left: 8px; }
  .card--front .wordmark__name { font-size: 60px; }
  .card--front .wordmark__tag { font-size: 31px; margin-top: 10px; }
  .card--back .wordmark { top: 138px; color: var(--on-brand); padding-left: 60px; }
  .card--back .wordmark__name { font-size: 58px; }
  .card--back .wordmark__tag { font-size: 30px; margin-top: 12px; }
  .divider {
    position: absolute; left: 0; right: 0; top: 171px; height: 7px;
    background: var(--brand-tint);
  }
  .identity {
    position: absolute; right: 387px; top: 232px; text-align: right;
  }
  .identity__name {
    font-family: "Montserrat", sans-serif; font-weight: 600;
    font-size: 34px; color: var(--name-grey); margin: 0; line-height: 1;
  }
  .identity__title {
    font-family: "Montserrat", sans-serif; font-weight: 300;
    font-size: 18px; color: var(--brand-tint); margin: 9px 0 0; line-height: 1;
  }
  .identity-rule {
    position: absolute; left: 297px; top: 228px; width: 1.5px; height: 80px;
    background: var(--brand-tint);
  }
  .contacts {
    position: absolute; left: 314px; top: 221px;
    margin: 0; padding: 0; list-style: none;
    font-family: "Jost", sans-serif; font-size: 15px; color: var(--brand-tint);
  }
  .contacts li {
    display: flex; align-items: center; height: 23px; white-space: nowrap;
  }
  .contacts svg { width: 13px; height: 13px; margin-right: 10px; fill: var(--name-grey); flex: none; }
</style>
</head>
<body>
<main class="stage">
  <section class="card card--front" aria-label="Contact side">
    <div class="card__pattern" role="img" aria-label="Faint repeating brand pattern in light grey"></div>
    <div class="wordmark">
      <span class="wordmark__name">CORVALE</span>
      <span class="wordmark__tag">SPINE &amp; JOINT</span>
    </div>
    <div class="divider"></div>
    <div class="identity">
      <p class="identity__name">Marcus Hale</p>
      <p class="identity__title">Founder/ceo</p>
    </div>
    <div class="identity-rule"></div>
    <ul class="contacts">
      <li><svg viewBox="0 0 16 16" aria-hidden="true"><path d="M3.5 1.5l2.5 0 1 3.5-1.7 1.2a9 9 0 0 0 4.5 4.5L11 9l3.5 1v2.5c0 1-1 2-2 2A11 11 0 0 1 1.5 3.5c0-1 1-2 2-2z"/></svg>222.555.0142 | 222.555.0142</li>
      <li><svg viewBox="0 0 16 16" aria-hidden="true"><path d="M1 3h14v10H1z M1.5 3.5L8 9l6.5-5.5" /></svg>hello@corvalespine.com</li>
      <li><svg viewBox="0 0 16 16" aria-hidden="true"><path d="M8 1a7 7 0 1 0 0 14A7 7 0 0 0 8 1zm0 1.4c.8.8 1.5 2.3 1.7 4.1H6.3C6.5 4.7 7.2 3.2 8 2.4zM2.5 7.5h2.4c.1-1.8.6-3.3 1.3-4.3A5.6 5.6 0 0 0 2.5 7.5zm0 1h2.4c.1 1.8.6 3.3 1.3 4.3a5.6 5.6 0 0 1-3.7-4.3zm3.8 0h3.4c-.2 1.8-.9 3.3-1.7 4.1-.8-.8-1.5-2.3-1.7-4.1zm4.8 0h2.4a5.6 5.6 0 0 1-3.7 4.3c.7-1 1.2-2.5 1.3-4.3zm0-1c-.1-1.8-.6-3.3-1.3-4.3a5.6 5.6 0 0 1 3.7 4.3z"/></svg>www.corvalespine.com</li>
      <li><svg viewBox="0 0 16 16" aria-hidden="true"><path d="M8 1a5 5 0 0 0-5 5c0 3.5 5 9 5 9s5-5.5 5-9a5 5 0 0 0-5-5zm0 7a2 2 0 1 1 0-4 2 2 0 0 1 0 4z"/></svg>Location, Street, Town Number</li>
    </ul>
  </section>

  <section class="card card--back" aria-label="Brand side">
    <div class="wordmark">
      <span class="wordmark__name">CORVALE</span>
      <span class="wordmark__tag">SPINE &amp; JOINT</span>
    </div>
  </section>
</main>
</body>
</html>
```